Vantrel Grace Dental offce
Professional
Jessa
Owner
2871 Fenwick Ln
Ashbridge, Pa
jessakweldon@mailbrook.com
I uploaded my logo on the intro page
Please let me know if there are any problems. 610-824-3917 or jessakweldon@mailbrook.com

```html
<!DOCTYPE html>
<html lang="en">
<head>
<meta charset="utf-8">
<title>Vantrel Grace Dental – Business Card</title>
<link href="https://fonts.googleapis.com/css2?family=Open+Sans:wght@400;600;700&display=swap" rel="stylesheet">
<style>
  :root {
    --bg: #d9d9d9;
    --card-white: #ffffff;
    --brand-orange: #f7941d;
    --brand-blue: #1f4e8c;
    --text-gray: #6d6e71;
    --text-light: #9a9b9d;
  }
  * { margin: 0; padding: 0; box-sizing: border-box; }
  html, body {
    width: 1200px;
    height: 901px;
    overflow: hidden;
    background: var(--bg);
    font-family: "Open Sans", Arial, sans-serif;
  }
  .stage {
    position: relative;
    width: 1200px;
    height: 901px;
  }
  .card {
    position: absolute;
    top: 307px;
    width: 500px;
    height: 286px;
    box-shadow: 0 6px 18px rgba(0,0,0,0.18);
  }
  .card-back {
    left: 70px;
    background: var(--brand-orange);
    display: flex;
    align-items: center;
    justify-content: center;
    gap: 12px;
  }
  .card-back .brand-dot {
    width: 16px; height: 16px; border-radius: 50%;
    background: var(--card-white);
  }
  .card-back .brand-name {
    color: var(--card-white);
    font-weight: 700;
    font-size: 26px;
    letter-spacing: 0.5px;
  }
  .card-front {
    left: 630px;
    background: var(--card-white);
  }
  .front-brand {
    position: absolute;
    left: 40px; top: 50px;
    display: flex; align-items: center; gap: 10px;
  }
  .front-brand .brand-dot {
    width: 14px; height: 14px; border-radius: 50%;
    background: var(--brand-orange);
  }
  .front-brand .brand-name {
    color: var(--brand-blue);
    font-weight: 700;
    font-size: 22px;
    letter-spacing: 0.5px;
  }
  .address {
    position: absolute;
    left: 42px; top: 126px;
    font-size: 11px;
    font-style: normal;
    line-height: 16px;
    color: var(--text-gray);
  }
  .contact-list {
    position: absolute;
    left: 42px; top: 190px;
    list-style: none;
    font-size: 11px;
    line-height: 18px;
    color: var(--text-gray);
  }
  .contact-list li { display: flex; align-items: center; gap: 7px; }
  .contact-list svg { width: 10px; height: 10px; }
  .icon-phone { fill: var(--brand-orange); }
  .icon-mail { fill: none; stroke: var(--brand-orange); stroke-width: 2.5; }
  .person {
    position: absolute;
    left: 350px; top: 194px;
  }
  .person-name {
    color: var(--brand-orange);
    font-weight: 700;
    font-size: 17px;
  }
  .person-role {
    color: var(--text-light);
    font-size: 9px;
  }
</style>
</head>
<body>
<main class="stage">
  <section class="card card-back" aria-label="Card back">
    <span class="brand-dot"></span>
    <span class="brand-name">Vantrel Grace Dental</span>
  </section>

  <section class="card card-front" aria-label="Card front">
    <div class="front-brand">
      <span class="brand-dot"></span>
      <span class="brand-name">Vantrel Grace Dental</span>
    </div>

    <address class="address">
      2871 Fenwick Ln<br>
      Ashbridge, Pa<br>
      18049
    </address>

    <ul class="contact-list">
      <li>
        <svg class="icon-phone" viewBox="0 0 24 24" aria-hidden="true"><path d="M6.6 10.8a15.1 15.1 0 0 0 6.6 6.6l2.2-2.2c.3-.3.7-.4 1-.2 1.1.4 2.3.6 3.6.6.6 0 1 .4 1 1V20c0 .6-.4 1-1 1A17 17 0 0 1 3 4c0-.6.4-1 1-1h3.5c.6 0 1 .4 1 1 0 1.3.2 2.5.6 3.6.1.3 0 .7-.2 1z"/></svg>
        610-824-3917
      </li>
      <li>
        <svg class="icon-mail" viewBox="0 0 24 24" aria-hidden="true"><path d="M2 5h20v14H2z M2 5l10 8 10-8"/></svg>
        jessakweldon@mailbrook.com
      </li>
    </ul>

    <div class="person">
      <div class="person-name">Jessa</div>
      <div class="person-role">Owner</div>
    </div>
  </section>
</main>
</body>
</html>
```